Author needs cover design for health related book

I need the front cover designed for an upcoming book. I want a cover that will stand out when viewed in a thumbnail on sites such as Brellix. I'm open to the color scheme. The cover design should convey hopeful, uplifting energy, trust, and confidence. Nothing cute or frilly, please. The book is written for newly diagnosed cancer patients. The book title is: The Test Came Back, So Where Next? Subtitle: Steadily Facing Illness Through Dread, Confusion and Worry
Author: Marvina Tobbel
I'm not window shopping. I will definitely pick one of the submitted designs.
Target Market(s)
Newly diagnosed cancer patients
Industry/Entity Type
Health Care
Look and feel

```html
<!DOCTYPE html>
<html lang="en">
<head>
<meta charset="utf-8">
<title>The Test Came Back, So Where Next? — Marvina Tobbel</title>
<link href="https://fonts.googleapis.com/css2?family=Bebas+Neue&family=Oswald:wght@500&family=Open+Sans:wght@600&display=swap" rel="stylesheet">
<style>
  :root {
    --sky-top: #a9d8ea;
    --sky-mid: #d9f2f9;
    --glow: #f6fdff;
    --water: #5bb8cc;
    --water-deep: #3f9fb5;
    --ink: #262a2e;
    --navy: #1f3140;
    --wing-light: #8fe0fa;
    --wing-mid: #45b4ec;
    --wing-deep: #2a86c8;
  }
  html, body {
    margin: 0;
    padding: 0;
    width: 800px;
    height: 1200px;
    overflow: hidden;
  }
  .cover {
    position: relative;
    width: 800px;
    height: 1200px;
    overflow: hidden;
    background:
      radial-gradient(ellipse 460px 420px at 50% 62%, var(--glow) 0%, rgba(246,253,255,0) 100%),
      linear-gradient(180deg, var(--sky-top) 0%, var(--sky-mid) 42%, #cdebf4 80%, var(--water) 91%, var(--water-deep) 100%);
  }
  .subtitle {
    position: absolute;
    top: 34px;
    left: 120px;
    right: 120px;
    margin: 0;
    text-align: center;
    font-family: "Open Sans", sans-serif;
    font-weight: 600;
    font-size: 27px;
    line-height: 1.3;
    color: var(--navy);
  }
  .title {
    position: absolute;
    top: 172px;
    left: 0;
    right: 0;
    margin: 0;
    text-align: center;
    font-family: "Bebas Neue", sans-serif;
    font-weight: 400;
    color: var(--ink);
    line-height: 0.9;
  }
  .title-line { display: block; }
  .title-lead { font-size: 88px; letter-spacing: 2px; }
  .title-main { font-size: 182px; letter-spacing: 6px; }
  .title-end { font-size: 96px; letter-spacing: 2px; }
  .butterfly-art {
    position: absolute;
    left: 120px;
    top: 530px;
    width: 560px;
    height: 460px;
    background:
      radial-gradient(ellipse closest-side at 50% 48%,
        var(--wing-light) 0%,
        var(--wing-mid) 35%,
        rgba(42,134,200,0.55) 60%,
        rgba(42,134,200,0) 100%);
  }
  .water-art {
    position: absolute;
    left: 0;
    bottom: 0;
    width: 800px;
    height: 170px;
    background: linear-gradient(180deg, rgba(91,184,204,0) 0%, rgba(63,159,181,0.55) 100%);
  }
  .author {
    position: absolute;
    left: 0;
    right: 0;
    bottom: 56px;
    margin: 0;
    text-align: center;
    font-family: "Oswald", sans-serif;
    font-weight: 500;
    font-size: 56px;
    letter-spacing: 1px;
    color: var(--navy);
  }
</style>
</head>
<body>
  <main class="cover">
    <p class="subtitle">Steadily Facing Illness Through Dread, Confusion and Worry</p>
    <h1 class="title">
      <span class="title-line title-lead">The Test Came</span>
      <span class="title-line title-main">Back, So</span>
      <span class="title-line title-end">Where Next?</span>
    </h1>
    <div class="butterfly-art" role="img" aria-label="Glowing blue butterfly surrounded by sparkles, floating above calm water"></div>
    <div class="water-art" role="img" aria-label="Calm water surface reflecting soft light"></div>
    <p class="author">Marvina Tobbel</p>
  </main>
</body>
</html>
```